Innovative psychologist for companies seeks web design for website

Psychologist offers 2 topics:
1. What can a company do to ensure that employees are satisfied and enjoy their work?
The following explanatory video is linked on the website:
https://www.vidplumora.com/watch?v=qTr8ZpLmW3d
2. How can you successfully change your own behavior?
Explanatory video: https://www.vidplumora.com/watch?v=HxK2vQeRt7b&t=6s
The slogan for the second theme will be: YOU are the pirate of your life!

Target Market(s)

companies and private individuals

Number of Pages Required

1 page

Requirements
Nice to have
• Characteristics of the psychologist: pragmatic, down-to-earth, honest, direct, appreciative, enjoys life, loves nature

```html
<!DOCTYPE html>
<html lang="en">
<head>
<meta charset="utf-8">
<title>Martin Hollberg – Psychologist</title>
<link rel="stylesheet" href="https://fonts.googleapis.com/css2?family=Montserrat:wght@400;500;600;700&display=swap">
<style>
:root{
  --orange:#e8432a;
  --orange-dark:#d8361f;
  --blue:#1b9ad6;
  --blue-dark:#1479b8;
  --ink:#1f2a37;
  --text:#4a5260;
  --white:#ffffff;
  --mist:#eef3f8;
  --footer:#f2f3f5;
}
*{margin:0;padding:0;box-sizing:border-box}
html,body{width:1200px;height:3576px;overflow:hidden}
body{font-family:'Montserrat',sans-serif;color:var(--ink);background:var(--white);position:relative}
a{color:inherit;text-decoration:none}
section,header,footer{position:absolute;left:0;width:1200px}
.abs{position:absolute}

/* hero */
.hero{top:0;height:840px;overflow:hidden}
.hero-photo{position:absolute;inset:0;background:linear-gradient(180deg,#9fb1c2 0%,#c9d3dc 35%,#8a97a6 62%,#4c5968 85%,#3b4653 100%)}
.brand{left:100px;top:34px;display:flex;align-items:center;gap:12px;color:var(--white);font-weight:700;font-size:22px;letter-spacing:.5px;white-space:nowrap}
.brand-dot{width:30px;height:30px;border-radius:50%;background:var(--white)}
.nav{left:456px;top:38px;display:flex;gap:30px;font-size:13px;font-weight:600;color:var(--white);text-transform:uppercase;white-space:nowrap}
.nav a.active{border-bottom:2px solid var(--white);padding-bottom:4px}
.phone-pill{left:972px;top:32px;background:var(--orange);color:var(--white);font-size:13px;font-weight:600;padding:7px 16px;border-radius:20px;display:flex;align-items:center;gap:8px;white-space:nowrap}
.hero-tag{left:112px;top:240px;background:var(--orange);color:var(--white);font-size:30px;font-weight:600;padding:4px 14px}
.hero-title{left:112px;top:292px;color:var(--white);font-size:58px;font-weight:500;line-height:1.12;text-transform:uppercase}
.btn{display:inline-block;border-radius:30px;color:var(--white);font-size:14px;font-weight:700;text-transform:uppercase;padding:15px 36px;white-space:nowrap}
.btn-blue{background:var(--blue)}
.btn-orange{background:var(--orange)}
.hero .btn{left:112px;top:424px}
.hero-wave{left:0;bottom:0}

/* about */
.about{top:840px;height:440px}
.about-frame-o{left:128px;top:-4px;width:300px;height:360px;background:var(--orange)}
.about-photo{left:150px;top:-26px;width:360px;height:360px;background:linear-gradient(160deg,#dfe6ec,#b89a86 55%,#6c7f95);border:6px solid var(--blue)}
.about-title{left:560px;top:0;font-size:40px;font-weight:500;color:var(--orange);white-space:nowrap}
.about-title .blue{color:var(--blue)}
.about-title .box{background:var(--blue);color:var(--white);padding:0 8px}
.about-text{left:560px;width:470px;font-size:16px;line-height:1.55;color:var(--text)}
.about .btn{left:560px;top:276px}

/* employees */
.employees{top:1300px;height:540px;background:linear-gradient(90deg,#fff 0%,#f3f6f9 50%,var(--mist) 100%)}
.h2{font-size:34px;font-weight:600;line-height:1.3;color:var(--ink)}
.hl{background:var(--orange);color:var(--white);padding:0 8px;-webkit-box-decoration-break:clone;box-decoration-break:clone}
.rule{width:60px;height:3px;background:var(--orange)}
.body-text{font-size:15px;line-height:1.6;color:var(--text)}
.emp-text{left:100px;top:160px;width:490px;display:flex;flex-direction:column;gap:18px}
.emp-text .h2{font-size:30px;line-height:1.4}
.video-frame{background:var(--orange)}
.video{display:block;overflow:hidden}
.play{position:absolute;left:50%;top:50%;width:74px;height:74px;margin:-37px 0 0 -37px}

/* behaviour */
.behaviour{top:1840px;height:720px;background:linear-gradient(180deg,#2f9ee0 0%,#1b8ad2 60%,#1c7fc6 100%);color:var(--white)}
.behaviour .h2{color:var(--white);text-align:center;width:1200px}
.behaviour .body-text{color:var(--white);text-align:center;width:1200px}

/* contact */
.contact{top:2560px;height:560px}
.card-back-b{left:134px;top:64px;width:300px;height:200px;background:var(--blue)}
.card-back-b2{left:780px;top:300px;width:310px;height:210px;background:var(--blue)}
.card{left:150px;top:80px;width:930px;height:420px;background:linear-gradient(135deg,#f05a2e,var(--orange) 50%,var(--orange-dark))}
.card-title{top:40px;width:930px;text-align:center;font-size:44px;font-weight:500;color:var(--white)}
.card-title .box{background:var(--blue);padding:0 10px}
.card-sub{top:112px;width:930px;text-align:center;font-size:15px;color:var(--white)}
.field{background:var(--white);font-size:12px;color:#7b828d;padding:14px 14px}
.contact .btn{left:528px;top:476px;border-radius:4px;padding:14px 40px;font-size:13px}

/* footer */
.site-footer{top:3120px;height:456px;background:var(--footer)}
.f-brand{left:60px;top:60px;width:260px;text-align:center}
.f-dot{width:60px;height:60px;border-radius:50%;background:var(--orange);margin:0 auto 12px}
.f-name{font-size:20px;font-weight:700;color:var(--orange);text-transform:uppercase;white-space:nowrap}
.socials{left:127px;top:176px;display:flex;gap:12px}
.socials span{width:34px;height:34px;border-radius:50%;background:var(--blue)}
.f-col h4{font-size:15px;font-weight:700;text-transform:uppercase;letter-spacing:.5px;margin-bottom:8px;white-space:nowrap}
.f-col .bar{width:40px;height:3px;background:var(--orange);margin-bottom:16px}
.f-col li{list-style:none;font-size:14px;color:var(--text);margin-bottom:12px;white-space:nowrap}
.f-contact li{display:flex;align-items:center;gap:10px}
.ico{width:26px;height:26px;border-radius:50%;background:var(--blue);display:flex;align-items:center;justify-content:center}
.f-line{left:100px;top:360px;width:1000px;height:1px;background:#d9dce1}
.copy{top:392px;width:1200px;text-align:center;font-size:13px;color:var(--text)}
</style>
</head>
<body>

<header class="hero">
  <div class="hero-photo" role="img" aria-label="Man on a mountain peak with arms raised above a misty valley"></div>
  <a class="abs brand" href="#"><span class="brand-dot"></span>MARTIN HOLLBERG</a>
  <nav class="abs nav">
    <a class="active" href="#">About</a>
    <a href="#behaviour">Change Behavior</a>
    <a href="#employees">Employees Satisfied</a>
    <a href="#contact">Contact</a>
  </nav>
  <a class="abs phone-pill" href="#"><svg width="14" height="14" viewBox="0 0 24 24"><path fill="#fff" d="M6.6 10.8a15 15 0 0 0 6.6 6.6l2.2-2.2c.3-.3.7-.4 1-.2 1.1.4 2.3.6 3.6.6.6 0 1 .4 1 1V20c0 .6-.4 1-1 1A17 17 0 0 1 3 4c0-.6.4-1 1-1h3.5c.6 0 1 .4 1 1 0 1.3.2 2.5.6 3.6.1.3 0 .7-.2 1z"/></svg>(+555) 019 2846</a>
  <div class="abs hero-tag">MARTIN HOLLBERG</div>
  <h1 class="abs hero-title">You are the pirate<br>of your life!</h1>
  <a class="abs btn btn-blue" href="#contact">Contact me</a>
  <svg class="abs hero-wave" width="1200" height="180" viewBox="0 0 1200 180">
    <path d="M0 120 C300 40 700 180 1200 70 L1200 180 L0 180Z" fill="#fff"/>
    <path d="M0 110 C300 30 700 170 1200 60" fill="none" stroke="#1b9ad6" stroke-width="10"/>
  </svg>
</header>

<section class="about">
  <div class="abs about-frame-o"></div>
  <div class="abs about-photo" role="img" aria-label="Portrait of the psychologist smiling"></div>
  <h2 class="abs about-title">About <span class="blue">Martin</span> <span class="box">Hollberg</span></h2>
  <p class="abs about-text" style="top:76px">Lorem ipsum dolor sit amet, consectetur adipiscing elit, sed do eiusmod tempor incididunt ut labore et dolore</p>
  <p class="abs about-text" style="top:150px">Aagna aliqua Ut enim ad minim veniam, quis nostrud exercitation ullamco laboris nisi ut aliquip ex ea commodo consequat. Duis aute irure dolor in reprehenderit in voluptate velit esse cillum dolore eu fu</p>
  <a class="abs btn btn-orange" href="#">Learn more</a>
</section>

<section class="employees" id="employees">
  <div class="abs emp-text">
    <h2 class="h2">What can a company do to ensure that employees are satisfied and <span class="hl">enjoy their work?</span></h2>
    <div class="rule"></div>
    <p class="body-text">Lorem ipsum dolor sit amet, consectetur adipiscing elit, sed do eiusmod tempor incididunt ut labore et dolore magna aliqua. Ut enim ad minim veniam, quis nostrud exercitation ullamco laboris nisi ut aliquip ex ea commodo consequat. Duis aute irure dolor in reprehenderit in voluptate velit esse cillum dolore eu fu</p>
  </div>
  <div class="abs video-frame" style="left:630px;top:110px;width:500px;height:260px"></div>
  <a class="abs video" href="https://www.vidplumora.com/watch?v=qTr8ZpLmW3d" style="left:610px;top:90px;width:500px;height:250px">
    <div role="img" aria-label="Cartoon of a manager and an employee shaking hands in an office" style="width:100%;height:100%;background:linear-gradient(180deg,#c7cfd8,#9fb0c2 60%,#7c8ea3)"></div>
    <svg class="play" viewBox="0 0 74 74"><circle cx="37" cy="37" r="35" fill="#1f2a37"/><path d="M30 24 L52 37 L30 50Z" fill="#fff"/></svg>
  </a>
</section>

<section class="behaviour" id="behaviour">
  <h2 class="abs h2" style="left:0;top:110px;font-size:38px">How can you <span class="hl">Successfully change</span><br>your own behavior?</h2>
  <div class="abs rule" style="left:570px;top:222px;background:#fff"></div>
  <p class="abs body-text" style="left:0;top:236px">Lorem ipsum dolor sit amet, consectetur adipiscing elit, sed do eiusmod tempor<br>incididunt ut labore et dolore magna aliqua. Ut enim ad minim veniam</p>
  <div class="abs" style="left:250px;top:290px;width:420px;height:240px;background:#163f66"></div>
  <div class="abs video-frame" style="left:540px;top:430px;width:400px;height:280px"></div>
  <a class="abs video" href="https://www.vidplumora.com/watch?v=HxK2vQeRt7b&t=6s" style="left:260px;top:300px;width:660px;height:400px">
    <div role="img" aria-label="Illustration of a man standing before an open garden gate in a maze" style="width:100%;height:100%;background:linear-gradient(180deg,#b9c3b4,#8fa085 50%,#6e7a62)"></div>
    <svg class="play" viewBox="0 0 74 74"><circle cx="37" cy="37" r="35" fill="none" stroke="#fff" stroke-width="4"/><path d="M30 24 L52 37 L30 50Z" fill="#fff"/></svg>
  </a>
</section>

<section class="contact" id="contact">
  <div class="abs card-back-b"></div>
  <div class="abs card-back-b2"></div>
  <div class="abs card">
    <h2 class="abs card-title">Get in touch <span class="box">with me</span></h2>
    <p class="abs card-sub">Leave us a message &amp; I will contact you shortly.</p>
    <div class="abs field" style="left:150px;top:196px;width:304px">First Name</div>
    <div class="abs field" style="left:466px;top:196px;width:314px">Last Name</div>
    <div class="abs field" style="left:150px;top:254px;width:304px">Email address</div>
    <div class="abs field" style="left:466px;top:254px;width:314px">Phone number</div>
    <div class="abs field" style="left:150px;top:312px;width:630px;height:90px">Message</div>
  </div>
  <a class="abs btn btn-blue" href="#">Send message</a>
</section>

<footer class="site-footer">
  <div class="abs f-brand"><div class="f-dot"></div><div class="f-name">Martin Hollberg</div></div>
  <div class="abs socials"><span></span><span></span><span></span></div>
  <div class="abs f-col" style="left:410px;top:60px">
    <h4>Navigation</h4><div class="bar"></div>
    <ul><li>Home</li><li>About Us</li><li>Videos</li><li>Contact us</li></ul>
  </div>
  <div class="abs f-col" style="left:600px;top:60px">
    <h4>Resources</h4><div class="bar"></div>
    <ul><li>Blogs</li><li>Terms of Use</li><li>Privacy Policy</li></ul>
  </div>
  <div class="abs f-col f-contact" style="left:820px;top:60px">
    <h4>Contact us</h4><div class="bar"></div>
    <ul>
      <li><span class="ico"><svg width="13" height="13" viewBox="0 0 24 24"><path fill="#fff" d="M6.6 10.8a15 15 0 0 0 6.6 6.6l2.2-2.2c.3-.3.7-.4 1-.2 1.1.4 2.3.6 3.6.6.6 0 1 .4 1 1V20c0 .6-.4 1-1 1A17 17 0 0 1 3 4c0-.6.4-1 1-1h3.5c.6 0 1 .4 1 1 0 1.3.2 2.5.6 3.6.1.3 0 .7-.2 1z"/></svg></span>(+555) 019 2846</li>
      <li><span class="ico"><svg width="13" height="13" viewBox="0 0 24 24"><rect x="3" y="6" width="18" height="12" rx="1" fill="none" stroke="#fff" stroke-width="2"/><path d="M3 7 L12 13 L21 7" fill="none" stroke="#fff" stroke-width="2"/></svg></span>info@martinhollberg.com</li>
    </ul>
  </div>
  <div class="abs f-line"></div>
  <p class="abs copy">Copyright 2024 Martin Hollberg. All Right Reserved.</p>
</footer>

</body>
</html>
```